Business Cards and Stationery Set
Curavend Healthcare
Professional
Teodor Lisk, MD
Managing Partner
4318 West Birch Lane, Suite 207-3
Fresno, CA 93520 USA
tlisk@curavendcare.example
www.curavendcare.example

```html
<!DOCTYPE html>
<html lang="en">
<head>
<meta charset="utf-8">
<title>Curavend Healthcare – Stationery Set</title>
<link href="https://fonts.googleapis.com/css2?family=Open+Sans:wght@400;600;700;800&display=swap" rel="stylesheet">
<style>
:root{
  --red:#c4161c;
  --red-dark:#7d0a0e;
  --ink:#2b2b2b;
  --grey:#6b6b6b;
  --paper:#ffffff;
  --stage:#3a3d40;
}
*{margin:0;padding:0;box-sizing:border-box}
html,body{width:1200px;height:799px;overflow:hidden}
body{background:var(--stage);font-family:"Open Sans",Arial,sans-serif;color:var(--ink);position:relative}
.sheet{position:absolute;background:var(--paper);overflow:hidden;box-shadow:0 3px 10px rgba(0,0,0,.45)}
.swoosh{position:absolute;left:0;top:0;width:100%}
.brand{position:absolute;display:flex;align-items:center;gap:6px;font-weight:800;color:var(--ink);white-space:nowrap}
.brand .dot{border-radius:50%;background:var(--red);flex:none}

/* letterhead */
.letterhead{left:50px;top:65px;width:579px;height:679px}
.letterhead .brand{left:20px;top:58px;font-size:20px}
.letterhead .brand .dot{width:20px;height:20px}
.letter{position:absolute;left:22px;top:110px;width:520px;font-size:6.5px;line-height:10px;color:#444}
.letter .recipient{margin-bottom:34px}
.letter p{margin-bottom:10px}
.letter .greeting{margin-bottom:10px}
.letter .closing{margin-top:40px}
.letter-foot{position:absolute;left:0;right:0;bottom:0;height:26px;border-top:2px solid var(--red);font-size:5.5px;color:#555;padding:8px 22px}

/* business card */
.card{left:672px;top:65px;width:449px;height:247px;border-radius:8px}
.card .holder{position:absolute;right:20px;top:12px;text-align:right}
.card .name{font-size:15px;font-weight:600;color:#555}
.card .role{font-size:8px;color:#666}
.card .brand{left:18px;top:140px;font-size:17px;gap:5px}
.card .brand .dot{width:16px;height:16px}
.card .contact{position:absolute;left:268px;top:92px;font-size:7px;line-height:11px;color:#444}

/* open envelope back */
.envelope-back{left:672px;top:336px;width:449px;height:230px}
/* envelope front */
.envelope-front{left:672px;top:581px;width:449px;height:163px}
.envelope-front .brand{left:18px;top:28px;font-size:19px}
.envelope-front .brand .dot{width:18px;height:18px}
.envelope-front .return{position:absolute;left:20px;top:58px;font-size:5.5px;line-height:8px;color:#555}
</style>
</head>
<body>

<section class="sheet letterhead" aria-label="Letterhead">
  <svg class="swoosh" viewBox="0 0 579 120" height="120" preserveAspectRatio="none">
    <defs>
      <linearGradient id="lhRed" x1="0" y1="0" x2="1" y2="0">
        <stop offset="0" stop-color="var(--red-dark)"/><stop offset=".5" stop-color="var(--red)"/><stop offset="1" stop-color="var(--red-dark)"/>
      </linearGradient>
    </defs>
    <path d="M0 0H579V92C420 48 230 14 0 20Z" fill="url(#lhRed)"/>
    <path d="M0 24C230 20 420 56 579 100" fill="none" stroke="#111" stroke-width="6"/>
    <path d="M0 32C230 30 420 66 579 112" fill="none" stroke="#999" stroke-width="1.5"/>
  </svg>
  <div class="brand"><span class="dot"></span>Curavend Healthcare</div>

  <div class="letter">
    <div class="recipient">Someone Somebody<br>100 Long St<br>Brisbane, Australia</div>
    <div class="greeting">Dear Someone Somebody,</div>
    <p>Lorem ipsum dolor sit amet, consectetuer adipiscing elit, sed diam nonummy nibh euismod tincidunt ut laoreet dolore magna aliquam erat volutpat. Ut wisi enim ad minim veniam, quis nostrud exerci tation ullamcorper suscipit lobortis nisl ut aliquip ex ea commodo consequat. Duis autem vel eum iriure dolor in hendrerit in vulputate velit esse molestie consequat.</p>
    <p>Lorem ipsum dolor sit amet, consectetuer adipiscing elit, sed diam nonummy nibh euismod tincidunt ut laoreet dolore magna aliquam erat volutpat. Ut wisi enim ad minim veniam, quis nostrud exerci tation ullamcorper suscipit lobortis nisl ut aliquip ex ea commodo consequat. Duis autem vel eum iriure dolor in hendrerit in vulputate velit esse molestie consequat.</p>
    <p>Lorem ipsum dolor sit amet, consectetuer adipiscing elit, sed diam nonummy nibh euismod tincidunt ut laoreet dolore magna aliquam erat volutpat. Ut wisi enim ad minim veniam, quis nostrud exerci tation ullamcorper suscipit lobortis nisl ut aliquip ex ea commodo consequat. Duis autem vel eum iriure dolor in hendrerit in vulputate velit esse molestie consequat.</p>
    <p>Lorem ipsum dolor sit amet, consectetuer adipiscing elit, sed diam nonummy nibh euismod tincidunt ut laoreet dolore magna aliquam erat volutpat. Ut wisi enim ad minim veniam, quis nostrud exerci tation ullamcorper suscipit lobortis nisl ut aliquip ex ea commodo consequat. Duis autem vel eum iriure dolor in hendrerit in vulputate velit esse molestie consequat.</p>
    <div class="closing">Nora Vale<br>Office Manager</div>
  </div>

  <div class="letter-foot">4318 West Birch Lane, Suite 207-3, Fresno, CA 93520 USA &nbsp;|&nbsp; Phone: +1 555 010 0142 &nbsp;|&nbsp; www.curavendcare.example</div>
</section>

<section class="sheet card" aria-label="Business card">
  <svg class="swoosh" viewBox="0 0 449 110" height="110" preserveAspectRatio="none">
    <defs>
      <linearGradient id="bcRed" x1="0" y1="0" x2="1" y2="0">
        <stop offset="0" stop-color="var(--red-dark)"/><stop offset=".6" stop-color="var(--red)"/><stop offset="1" stop-color="var(--red-dark)"/>
      </linearGradient>
    </defs>
    <path d="M0 0H230C200 30 120 70 0 95Z" fill="url(#bcRed)"/>
    <path d="M230 0C200 34 120 76 0 102" fill="none" stroke="#111" stroke-width="5"/>
    <path d="M245 0C214 40 130 84 0 110" fill="none" stroke="#999" stroke-width="1.2"/>
  </svg>
  <div class="holder">
    <div class="name">Teodor Lisk, MD</div>
    <div class="role">Managing Partner</div>
  </div>
  <div class="brand"><span class="dot"></span>Curavend Healthcare</div>
  <div class="contact">
    4318 West Birch Lane<br>Suite 207-3<br>Fresno, CA 93520 USA<br><br>
    p: +1 555 010 0142<br>f: +1 555 010 0143<br>
    e: tlisk@curavendcare.example<br>www.curavendcare.example
  </div>
</section>

<section class="sheet envelope-back" aria-label="Envelope back with flap">
  <svg viewBox="0 0 449 230" width="449" height="230">
    <defs>
      <linearGradient id="evRed" x1="0" y1="0" x2="0" y2="1">
        <stop offset="0" stop-color="var(--red-dark)"/><stop offset="1" stop-color="var(--red)"/>
      </linearGradient>
    </defs>
    <rect width="449" height="230" fill="#f4f4f4"/>
    <path d="M0 230L180 150H269L449 230Z" fill="#e6e6e6"/>
    <path d="M0 0H449V40L224.5 150L0 40Z" fill="url(#evRed)"/>
    <path d="M0 40L224.5 150L449 40" fill="none" stroke="#111" stroke-width="5"/>
    <path d="M0 52L224.5 162L449 52" fill="none" stroke="#bbb" stroke-width="1.5"/>
    <circle cx="224.5" cy="45" r="13" fill="#fff"/>
    <circle cx="224.5" cy="128" r="12" fill="#fff"/>
  </svg>
</section>

<section class="sheet envelope-front" aria-label="Envelope front">
  <svg class="swoosh" viewBox="0 0 449 80" height="80" preserveAspectRatio="none">
    <defs>
      <linearGradient id="efRed" x1="0" y1="0" x2="1" y2="0">
        <stop offset="0" stop-color="var(--red)"/><stop offset="1" stop-color="var(--red-dark)"/>
      </linearGradient>
    </defs>
    <path d="M200 0H449V75C370 40 290 14 200 0Z" fill="url(#efRed)"/>
    <path d="M185 0C285 12 370 40 449 80" fill="none" stroke="#111" stroke-width="4"/>
  </svg>
  <div class="brand"><span class="dot"></span>Curavend Healthcare</div>
  <div class="return">4318 West Birch Lane, Suite 207-3<br>Fresno, CA 93520 USA</div>
</section>

</body>
</html>
```